New Business Card Design Project

The look of the business cards should include
-Clean Lines
-Should suit a sophisticated customer
-Evoke a mix of business and creativity
-Incorporate the color Gray or Black:White palette
-Open to see layouts in both vertical and horizontal
3 partners (we need 3 cards)
DORENE VASK
ELKE TARNOWSKI
NENA QUASTIGO
Reason: We would like more submissions please
Target Market(s)
We are a NYC and European based boutique consulting agency specializing in fashion business and creative clients. In addition to consulting we will be offering an e-commerce site selling women’s accessories and jewelry geared towards fashion forward women ages 25-50.
Industry/Entity Type
Business
Requirements
Must have
- - texture
- grayscale
3 Partners
Details for each card
CONSULTING I DESIGN
NENA QUASTIGO
Founding Partner
646.208.3371
nenA@themarlowtidecollective.com
www.themarlowtidecollective.com
CONSULTING I DESIGN
DORENE VASK
Founding Partner
646.851.2907
dorene@themarlowtidecollective.com
www.themarlowtidecollective.com
CONSULTING I DESIGN
Elke Dunsford Tarnowski
Founding Partner
(no phone for her)
Elke@themarlowtidecollective.com
www.themarlowtidecollective.com

```html
<!DOCTYPE html>
<html lang="en">
<head>
<meta charset="utf-8">
<title>The Marlow Tide Collective — Business Card</title>
<link rel="stylesheet" href="https://fonts.googleapis.com/css2?family=Source+Sans+3:wght@300;400&display=swap">
<style>
  :root {
    --backdrop: #e4e3e6;
    --card: #ffffff;
    --ink: #2f2f31;
    --ink-soft: #3c3c3e;
    --edge: rgba(0, 0, 0, 0.12);
  }
  * { box-sizing: border-box; margin: 0; padding: 0; }
  html, body {
    width: 1200px;
    height: 900px;
    overflow: hidden;
  }
  body {
    background: var(--backdrop);
    font-family: "Source Sans 3", "Helvetica Neue", Arial, sans-serif;
    color: var(--ink);
    display: flex;
    align-items: center;
    justify-content: center;
    gap: 64px;
  }
  .card {
    width: 500px;
    height: 286px;
    background: var(--card);
    box-shadow: 0 1px 0 var(--edge), 0 8px 22px rgba(0, 0, 0, 0.10);
    display: flex;
    flex-direction: column;
    align-items: center;
    justify-content: center;
  }
  .card-front .brand {
    display: flex;
    align-items: center;
    gap: 14px;
    font-weight: 300;
    font-size: 22px;
    letter-spacing: 0.32em;
    color: var(--ink);
    text-transform: uppercase;
  }
  .brand-square {
    width: 14px;
    height: 14px;
    background: var(--ink);
  }
  .card-back .services {
    font-weight: 300;
    font-size: 42px;
    letter-spacing: 0.01em;
    color: var(--ink-soft);
    margin-bottom: 18px;
  }
  .card-back .partner-name {
    font-weight: 400;
    font-size: 30px;
    line-height: 1;
    color: var(--ink-soft);
  }
  .card-back .partner-title {
    font-size: 13px;
    margin-top: 3px;
    margin-bottom: 14px;
  }
  .card-back .contact {
    list-style: none;
    text-align: center;
    font-size: 15px;
    line-height: 1.6;
  }
</style>
</head>
<body>
  <section class="card card-front" aria-label="Card front">
    <div class="brand">
      <span class="brand-square" aria-hidden="true"></span>
      <span class="brand-name">The Marlow Tide Collective</span>
    </div>
  </section>

  <section class="card card-back" aria-label="Card back">
    <h1 class="services">CONSULTING I DESIGN</h1>
    <h2 class="partner-name">NENA QUASTIGO</h2>
    <p class="partner-title">Founding Partner</p>
    <ul class="contact">
      <li>646.208.3371</li>
      <li>nenA@themarlowtidecollective.com</li>
      <li>www.themarlowtidecollective.com</li>
    </ul>
  </section>
</body>
</html>
```